Social Media Tool / Marketing Tool homepage design

We need a design template for a website to promote a web based technology / service. The product provide companies with a tools to generate business from social media web site.

We would like a homepage designed and an inner page of the site. This can be a contact us page or a sign up screen... Would also be good to have a design for the blog page of the site and static page i.e affiliates or advertiser page.

The feel of the site should reflect the fact that this is a social media tool but should not be too casual as we will have business clients so a blend between informal, practical and should communicate to business people (professional marketers)

Site should look friendly, thinking rounded edges rather than squared.

We have included logo design and like the idea of using the haxagonal shapes on the background in some way... Also included link to black on black design mock up that's not right as it's too heavy and does not appeal to any of the women we have shown it to. (50% of our audience)

http://mockups.brindlevault-studio.example/ORB/showcase/html/mockup3.html

http://mockups.brindlevault-studio.example/ORB/showcase/html/mockup1_2.html

http://mockups.brindlevault-studio.example/ORB/showcase/html/inner-page1.html

Above link to design that's not right. The taxonomy is right just not the black on black design. We are happy to use black but not black on a black background.

Please consider that we have 4 user types we are trying to sell to on this page hence the 4 blocks on the homepage. Feel free to interparate this how you will could be good as hexagons? or blocks??

Have attached a powerpoint of site pages please take homepage and dummy content and sign up / form page or contact page.

I have also attached logos please only use logo with one coloured hexagon the other file (logo) does not have the hexagon coloured but does include a set of icons that could also be used.

logo font = Metrostyle extended

Target Market(s)

Young professional marketers at bluechip businesses. User of social media sites like pormbly / quillnest and chirvo.

Industry/Entity Type

Business

Requirements
Must have
• should include pormbly, chirvo and quillnest icons (these will link to our profiles on these sites) Should feel friendly yet established, should feel social as this is a tool to market via social media. rounded edges / corners.
Should not have
• not old style fonts not fonts like times roman .. no squared (hard) corners.

```html
<!DOCTYPE html>
<html lang="en">
<head>
<meta charset="utf-8">
<title>Hexa-Pulse – Advocacy Marketing Platform</title>
<link href="https://fonts.googleapis.com/css2?family=Source+Sans+3:wght@400;600;700&display=swap" rel="stylesheet">
<style>
:root{
  --orange:#f07a1c;
  --orange-dark:#e0600e;
  --orange-light:#fbb25f;
  --cream:#fdf3ea;
  --ink:#333333;
  --grey:#6b6b6b;
  --nav:#2b2b2b;
  --card:#f3f3f3;
  --panel-inner:#fde2b0;
  --white:#ffffff;
}
*{box-sizing:border-box;margin:0;padding:0}
html,body{width:1200px;height:938px;overflow:hidden}
body{font-family:"Source Sans 3",Arial,sans-serif;color:var(--ink);position:relative;
  background:linear-gradient(180deg,var(--orange) 0,var(--orange) 29px,var(--cream) 29px,var(--cream) 126px,#f59a3f 126px,#fbc691 230px,#fdeee0 330px,#ffffff 420px,#ffffff 100%);}
.brand{position:absolute;left:196px;top:52px;font-size:33px;font-weight:700;color:#3b3b3b;letter-spacing:.5px}
.login{position:absolute;left:679px;top:40px;display:flex;gap:8px;align-items:center}
.login .field{width:128px;height:21px;border-radius:4px;background:#ececec;border:1px solid #d6d6d6;font-size:11px;color:#999;padding:3px 8px}
.login .btn{margin-left:2px;width:52px;height:19px;border-radius:3px;background:linear-gradient(#fa9a3a,var(--orange-dark));color:#fff;font-size:10px;font-weight:700;text-align:center;line-height:19px}
.login-help{position:absolute;right:193px;top:73px;font-size:10px;color:#333}
.login-help b{color:var(--orange-dark);font-size:11px}
.nav{position:absolute;left:475px;top:94px;width:725px;height:32px;background:linear-gradient(#3a3a3a,#1e1e1e);
  clip-path:polygon(20px 0,100% 0,100% 100%,0 100%);display:flex;align-items:center;padding-left:36px;gap:28px}
.nav a{color:#fff;text-decoration:none;font-size:11px;font-weight:600}
.nav a.active{color:#f7a02e}
.hero{position:absolute;left:181px;top:140px;width:835px;height:271px;border-radius:8px;overflow:hidden;
  background:linear-gradient(120deg,#c8cfd8,#eef0f2 40%,#b9b3ad 70%,#8c97a6)}
.hero-caption{position:absolute;left:0;bottom:0;width:100%;height:66px;background:rgba(40,40,40,.72);padding:10px 17px}
.hero-caption .kicker{color:#f8a21a;font-size:14px;font-weight:700}
.hero-caption h1{color:#fff;font-size:24px;font-weight:700;line-height:1.2;margin-top:2px}
.newsletter{position:absolute;right:17px;bottom:9px;width:204px;height:44px;border-radius:5px;background:linear-gradient(#fa9a3a,var(--orange-dark));color:#fff;text-align:right;padding:4px 12px}
.newsletter small{display:block;font-size:10px;font-weight:600;line-height:1.1;margin-right:20px}
.newsletter span{font-size:23px;font-weight:700;line-height:1}
.newsletter .mail{position:absolute;left:10px;top:6px}
.card{position:absolute;width:266px;height:207px;border-radius:8px;background:linear-gradient(#fbfbfb,var(--card));border:1px solid #e4e4e4}
.card h2{position:absolute;left:16px;top:17px;font-size:24px;font-weight:400;color:#333}
.card .more{position:absolute;right:16px;top:30px;font-size:9px;color:var(--orange-dark);font-weight:600}
.card .icon{position:absolute;left:18px;top:73px;width:80px;height:80px;border-radius:50%;border:4px solid #444;
  background:radial-gradient(circle at 40% 35%,#ffc56a,var(--orange) 55%,#a8440a)}
.card ul{position:absolute;left:120px;top:64px;width:140px;list-style:none;font-size:10.5px;line-height:15px}
.card li{padding-left:10px;position:relative;margin-bottom:5px}
.card li::before{content:">";position:absolute;left:0;color:var(--orange)}
.btn-register{position:absolute;left:121px;top:169px;width:120px;height:27px;border-radius:3px;background:linear-gradient(#fa9a3a,var(--orange-dark));color:#fff;font-size:13.5px;font-weight:700;text-align:center;line-height:27px}
.panel{position:absolute;left:755px;top:441px;width:261px;height:423px;border-radius:8px;background:linear-gradient(#f58a3a,#f27c28)}
.panel .users{position:absolute;left:17px;top:24px}
.panel h3{position:absolute;left:59px;top:20px;color:#fff;font-size:15px;font-weight:600;line-height:20px}
.panel h3 span{font-weight:400;color:#fde6cc}
.panel-body{position:absolute;left:7px;top:88px;width:248px;height:327px;border-radius:6px;background:linear-gradient(#fdd9a6,#fff1c4);padding:18px 14px;font-size:10.5px;line-height:20px}
.panel-body ul{list-style:none;margin-top:8px;width:220px}
.panel-body li{padding-left:10px;position:relative}
.panel-body li::before{content:">";position:absolute;left:0;color:var(--orange)}
.talk{position:absolute;right:10px;top:212px;width:105px;height:88px;border-radius:50%;background:radial-gradient(#ffffff,#d8d8d8)}
.btn-read{position:absolute;left:16px;top:279px;width:98px;height:27px;border-radius:3px;background:linear-gradient(#fa9a3a,var(--orange-dark));color:#fff;font-size:13.5px;font-weight:700;text-align:center;line-height:27px}
.footer{position:absolute;left:0;top:892px;width:1200px;height:46px;background:linear-gradient(#f58a2c,#f7a34d);font-size:11px;color:#fff}
.footer .links{position:absolute;left:198px;top:17px}
.footer .follow{position:absolute;left:858px;top:16px;display:flex;align-items:center;gap:9px}
.footer .sq{width:14px;height:14px;border-radius:3px;background:#fff;opacity:.9}
</style>
</head>
<body>
<header>
  <div class="brand">Hexa-Pulse</div>
  <div class="login"><div class="field">Member Login</div><div class="field">Password</div><div class="btn">LOGIN ▸</div></div>
  <div class="login-help">Forgot your Password? | Not a Member? <b>Sign Up!</b></div>
  <nav class="nav"><a>HOME</a><a>WHAT?</a><a>WHY?</a><a class="active">DEMO</a><a>REPORTS</a><a>BLOG</a><a>PRICING</a><a>CONTACT US</a></nav>
</header>

<section class="hero" role="img" aria-label="Photo of smiling business team meeting around a laptop">
  <div class="hero-caption">
    <div class="kicker">Demand Generation, Social Engagement and</div>
    <h1>Advocacy Marketing Platform</h1>
  </div>
  <div class="newsletter">
    <svg class="mail" width="34" height="32" viewBox="0 0 34 32"><rect x="2" y="6" width="30" height="22" rx="2" fill="#fff"/><path d="M2 8 L17 19 L32 8" fill="none" stroke="#e0600e" stroke-width="2"/></svg>
    <small>SUBSCRIBE FOR</small><span>Newsletter »</span>
  </div>
</section>

<article class="card" style="left:181px;top:441px">
  <h2>Advertisers</h2><span class="more">MORE +</span>
  <div class="icon" role="img" aria-label="Megaphone icon"></div>
  <ul><li>Create polls and surveys</li><li>Create competitions</li><li>Create B2B and B2C demand generation campaigns</li></ul>
  <div class="btn-register">Register Now! &gt;</div>
</article>
<article class="card" style="left:466px;top:441px">
  <h2>Advocates</h2><span class="more">MORE +</span>
  <div class="icon" role="img" aria-label="Figure holding a puzzle piece icon"></div>
  <ul><li>Choose from both D2C or B2B campaigns</li><li>Paid per lead</li><li>Full marketing tool kit</li></ul>
  <div class="btn-register">Register Now! &gt;</div>
</article>
<article class="card" style="left:181px;top:661px">
  <h2>Affiliates</h2><span class="more">MORE +</span>
  <div class="icon" role="img" aria-label="Handshake icon"></div>
  <ul><li>10% revenue share for tier one referrals</li><li>5% revenue share for second tier referrals</li><li>Real time reporting</li></ul>
  <div class="btn-register">Register Now! &gt;</div>
</article>
<article class="card" style="left:466px;top:661px">
  <h2>Agencies</h2><span class="more">MORE +</span>
  <div class="icon" role="img" aria-label="Presentation chart icon"></div>
  <ul><li>White label solution, upload logo or update CSS for full brand control</li><li>Build web forms to capture lead data</li><li>Cloudledger extension</li></ul>
  <div class="btn-register">Register Now! &gt;</div>
</article>

<aside class="panel">
  <svg class="users" width="34" height="34" viewBox="0 0 34 34"><circle cx="12" cy="10" r="6" fill="#fff"/><path d="M1 30 Q1 17 12 17 Q23 17 23 30Z" fill="#fff"/><circle cx="23" cy="8" r="5" fill="#fde6cc"/><path d="M18 15 Q32 13 33 27 L24 27Z" fill="#fde6cc"/></svg>
  <h3><span>Generate Lead via</span><br>Social Media Email and<br>Our Publisher Network...</h3>
  <div class="panel-body">
    <p><b>Hexa-Pulse.com</b> is a platform that allows advertisers to easily create surveys and lead generation campaigns and publish them across the social web.</p>
    <ul>
      <li>Create branded campaign landing pages without involving IT or any technical skills</li>
      <li>Engage with your audience on the social web, survery them for insights</li>
      <li>Generate leads from quillnest, chirvo and pormbly</li>
      <li>Reduce your sales cycle by providing your</li>
    </ul>
    <div class="talk" role="img" aria-label="Illustration of two business people talking on a speech bubble"></div>
    <div class="btn-read">Read More &gt;</div>
  </div>
</aside>

<footer class="footer">
  <div class="links">About Us | Contact Us | Sitemap | Privacy Policy</div>
  <div class="follow">Follow us <span class="sq"></span><span class="sq"></span><span class="sq"></span><span class="sq"></span></div>
</footer>
</body>
</html>
```